Moss & Lantern podcast needs new cover art

Our podcast, Moss & Lantern, is looking for a new design for an updated cover art. We are a podcast that talks about public relations (PR) stories each week, political news and political communications. While we are a professional podcast, the hosts of the show are brothers and their personalities (and humor) are important to the podcast. The artwork should reflect this. Our current artwork is attached. We are not opposed to using the photo of us, but we would like to see some designs without the photo as well.

Font styles to use
Sans Serif

Colors

Designer to choose colors to be used in the design.

Requirements
Nice to have
• Elements that convey both PR (communications) and politics. So for example, maybe a microphone and stars or a microphone and the U.S. Capitol building.

```html
<!DOCTYPE html>
<html lang="en">
<head>
<meta charset="UTF-8">
<title>Moss &amp; Lantern — Podcast Cover</title>
<link rel="stylesheet" href="https://fonts.googleapis.com/css2?family=Big+Shoulders+Display:wght@100&display=swap">
<style>
  :root {
    --gold: #e3a83a;
    --slate-blue: #8ea2c1;
    --cream: #f8ebdd;
    --photo-warm: #d8c9a8;
    --photo-mid: #8f8a7e;
    --photo-navy: #1f2a44;
    --photo-gray: #6f7580;
  }
  * { margin: 0; padding: 0; box-sizing: border-box; }
  html, body {
    width: 1200px;
    height: 1200px;
    overflow: hidden;
    background: var(--photo-mid);
  }
  .cover {
    position: relative;
    width: 1200px;
    height: 1200px;
    overflow: hidden;
    font-family: "Big Shoulders Display", "Arial Narrow", sans-serif;
  }
  .cover__photo {
    position: absolute;
    inset: 0;
    background:
      radial-gradient(ellipse 34% 60% at 25% 70%, var(--photo-navy) 0%, rgba(31,42,68,0.85) 55%, rgba(31,42,68,0) 100%),
      radial-gradient(ellipse 36% 62% at 75% 70%, var(--photo-gray) 0%, rgba(111,117,128,0.85) 55%, rgba(111,117,128,0) 100%),
      linear-gradient(180deg, #c9b48a 0%, var(--photo-warm) 30%, var(--photo-mid) 70%, #5b5a56 100%);
  }
  .title {
    position: absolute;
    inset: 0;
    text-transform: uppercase;
    font-weight: 100;
    line-height: 1;
  }
  .title__row {
    position: absolute;
    left: 112px;
    display: flex;
    align-items: baseline;
    gap: 36px;
    white-space: nowrap;
  }
  .title__row--top { top: 440px; }
  .title__row--bottom { top: 830px; }
  .title__first {
    font-size: 440px;
    color: var(--gold);
    letter-spacing: 4px;
  }
  .title__amp {
    font-size: 280px;
    color: var(--slate-blue);
  }
  .title__second {
    font-size: 340px;
    color: var(--cream);
    letter-spacing: 14px;
  }
</style>
</head>
<body>
  <main class="cover">
    <div class="cover__photo" role="img" aria-label="Photo of the two host brothers in blazers standing side by side outdoors in front of a fence at golden hour"></div>
    <h1 class="title">
      <span class="title__row title__row--top">
        <span class="title__first">Moss</span>
        <span class="title__amp">&amp;</span>
      </span>
      <span class="title__row title__row--bottom">
        <span class="title__second">Lantern</span>
      </span>
    </h1>
  </main>
</body>
</html>
```